Custom Header Designs - Automotive Parts - Alternator & Starter

We need 8 Header/Hero designs that will be used on our website. We are a company based in Montreal Canada and we re-manufacture Alternators and Starters for all types of vehicles. We offer a premium product and we are looking for premium designs that reflect the look of our packaging and the look of our website. Essentially we specialize in the sale and manufacture of two specific parts that go on all types of vehicles, Alternators and Starters. All text on these designs need to be editable as we will need to translate them to French once we get the source files.
Here are some websites of our competitors so you can draw some inspiration and see what our industry/business is all about:
https://www.qelvorparts.com/
https://www.zentrihaul.com/
Article that describes a remanufactured product, https://www.wombrixo.com/articles/starters-and-alternators-reman-vs-new.html
Our packaging is modern, sleek and professional. Our website is a B2B E-Commerce Site as well as an info site to promote our products. It is clean and minimal but we want the header/hero designs to help it stand out. Our main colors are blue and gray (as seen in our logo), but you can use whatever you like to compliment these colors.
Our packaging design was done on PixelTroupe, here is the link to that project so that you can see the packaging look and use any of the info that is from that project.
https://jobs.pixeltroupe.ca/job/5829463
The 8 Header/Hero designs will be used in the following areas, I have included a brief description of what we are looking for:
1 - Homepage Header/Hero image - This will be the homepage hero image therefore it should summarize the info described below. We offer premium quality re-manufactured alternators and starters. We are a wholesaler/distributor that services major auto-part stores with these quality products.
2 - General Product Header/Hero image - This image will be used as a header where the customer can learn general info about our products and any custom work we can do. This page will have a section where you can click to learn more about our individual product lines (links to product specific pages mentioned below) and a description of the custom work we can perform. We offer a two year manufacturers warranty.
3 - Alternator Product Header/Hero image - This image will be used to showcase our Alternator Product Line. Its purpose is to promote and advertise our premium re-manufactured alternators. This page will provide detailed info about our alternator re-manufacturing process and describe why our alternators are great.
4 - Starter Product Header/Hero image - This image will be used to showcase our Starter Product Line. Its purpose is to promote and advertise our premium re-manufactured starters. This page will provide detailed info about our starter re-manufacturing process and describe why our starters are great.
5 - General Header/Hero Image - This image will be used in most of our standard pages like our terms and conditions, privacy policy, warranty policy, our company page, etc. It needs to relate to the industry but be general enough so that we could use it in multiple areas
6 - Online Ordering Header image - This image will be used in our B2B area to introduce our customers to the Online Ordering system, its purpose is to advertise and explain some of the features of the Online Ordering system.
7 - B/O Re-Manufacture & Return Header Image - This image will be used in our B2B area to explain and advertise to our customers how our Backorder/R&R process works on our website. Essentially if we do not have the remanufactured part in stock but we have the core you could put the product on Backorder and we will remanufacture it in a few hours. If for any reason (rare vehicle, old vehicle, etc.) we do not have the core we will R&R (Remanufacture and Return) the customers core for them.
8 - Bulk Ordering Form Header Image - This image will be used in our B2B area to explain and advertise to our customers how our Bulk Ordering Form works on our website.
These hero/header images will be going on a Plankly/TillNest website and I am suggesting these images have a size of 1600 x 500, but we will take any other suggestions from the designers as you are the experts.
I have included a zip file that includes images of various elements that will help you in the design process.
Target Market(s)
Educate consumers about our products and attract auto supply chains to become distributors of our products.
Industry/Entity Type
Automotive Part

```html
<!DOCTYPE html>
<html lang="en">
<head>
<meta charset="utf-8">
<title>Korvane — Home</title>
<link rel="stylesheet" href="https://fonts.googleapis.com/css2?family=Arimo:wght@400;700&family=Montserrat:wght@500;700;800&display=swap">
<style>
  :root {
    --topbar-bg: #f2f2f3;
    --link-blue: #3c5aa8;
    --brand-blue: #25409a;
    --nav-gray: #5a5d63;
    --muted-gray: #8a8d92;
    --ink: #2d2f33;
    --navy-top: #0b2150;
    --navy-mid: #061636;
    --navy-deep: #01060f;
    --stat-bg: #06173a;
    --divider: rgba(255,255,255,0.28);
    --badge: #a6d6ec;
    --white: #ffffff;
    --silver-light: #f7f7f8;
    --silver-dark: #8e9298;
  }
  * { box-sizing: border-box; margin: 0; padding: 0; }
  html, body { width: 1200px; height: 794px; overflow: hidden; background: var(--white); }
  body { font-family: "Arimo", Arial, sans-serif; position: relative; }

  /* Utility bar */
  .utility-bar {
    position: absolute; left: 0; top: 0; width: 1200px; height: 29px;
    background: var(--topbar-bg); font-size: 12px;
  }
  .utility-bar > * { position: absolute; top: 8px; white-space: nowrap; }
  .utility-bar a { color: var(--link-blue); text-decoration: none; }
  .consult-link { left: 91px; }
  .call-line { left: 552px; color: var(--muted-gray); }
  .call-line strong { color: var(--ink); font-weight: 700; letter-spacing: .3px; }
  .bar-sep { left: 713px; color: var(--muted-gray); }
  .map-link { left: 731px; }
  .dashboard-link { left: 879px; top: 9px !important; font-size: 10px; letter-spacing: .2px; text-transform: uppercase; }
  .language { left: 1033px; top: 9px !important; font-size: 9.5px; color: var(--nav-gray); display: flex; align-items: center; gap: 3px; }
  .language svg { display: block; }

  /* Main header */
  .site-header {
    position: absolute; left: 0; top: 29px; width: 1200px; height: 90px; background: var(--white);
  }
  .brand {
    position: absolute; left: 102px; top: 26px; display: flex; align-items: center; gap: 10px;
    font-family: "Arimo", Arial, sans-serif; font-weight: 700; font-size: 34px; color: var(--brand-blue);
  }
  .brand-dot { width: 30px; height: 30px; border-radius: 50%; background: var(--brand-blue); }
  .main-nav { position: absolute; top: 35px; left: 0; font-size: 14px; color: var(--nav-gray); }
  .main-nav a { position: absolute; white-space: nowrap; color: inherit; text-decoration: none; }
  .cart { position: absolute; left: 1072px; top: 38px; }
  .cart-badge {
    position: absolute; left: 1091px; top: 27px; width: 18px; height: 18px; border-radius: 50%;
    background: var(--badge); color: var(--link-blue); font-size: 8px; text-align: center; line-height: 18px;
  }

  /* Hero */
  .hero { position: absolute; left: 0; top: 119px; width: 1200px; height: 675px; overflow: hidden; }
  .hero-dark {
    position: absolute; left: 0; top: 0; width: 829px; height: 675px;
    background: linear-gradient(175deg, var(--navy-top) 0%, var(--navy-mid) 50%, var(--navy-deep) 100%);
  }
  .hero-light {
    position: absolute; left: 829px; top: 0; width: 371px; height: 675px;
    background: linear-gradient(180deg, var(--white) 0%, #e4e5e7 45%, #9a9ea4 80%, #5d6168 100%);
  }
  .hero-bands { position: absolute; left: 0; top: 0; }
  .product-photo {
    position: absolute; left: 668px; top: 134px; width: 390px; height: 350px; border-radius: 46% 40% 44% 48%;
    background: radial-gradient(circle at 40% 45%, #f1f1f1 0%, #c9c9c9 45%, #7a7a7a 80%, #3b3b3b 100%);
  }
  .product-reflection {
    position: absolute; left: 672px; top: 480px; width: 380px; height: 190px; border-radius: 40% 40% 0 0;
    background: linear-gradient(180deg, rgba(150,155,165,.35), rgba(150,155,165,0));
  }
  .hero-title {
    position: absolute; left: 84px; top: 270px; font-family: "Montserrat", sans-serif; font-weight: 700;
    font-size: 74px; letter-spacing: .5px; line-height: 1;
    background: linear-gradient(180deg, var(--white) 30%, var(--silver-dark) 100%);
    -webkit-background-clip: text; background-clip: text; color: transparent;
  }
  .hero-copy {
    position: absolute; left: 88px; top: 369px; width: 440px; color: var(--white);
    font-size: 15px; line-height: 21.5px;
  }
  .stats {
    position: absolute; left: 86px; top: 467px; width: 420px; height: 109px;
    background: var(--stat-bg); border-radius: 8px; display: flex; color: var(--white); text-align: center;
  }
  .stat { display: flex; flex-direction: column; align-items: center; padding-top: 17px; }
  .stat + .stat { border-left: 1px solid var(--divider); }
  .stat:nth-child(1) { width: 130px; }
  .stat:nth-child(2) { width: 148px; margin: 16px 0; padding-top: 1px; }
  .stat:nth-child(3) { width: 142px; margin: 16px 0; padding-top: 1px; }
  .stat-value { font-family: "Montserrat", sans-serif; font-weight: 700; font-size: 36px; line-height: 38px; }
  .stat-label { font-size: 15px; line-height: 17px; margin-top: 3px; letter-spacing: .3px; }
  .stat-note { font-size: 10px; line-height: 12px; }
  .cta {
    position: absolute; left: 88px; top: 638px; width: 222px; height: 47px; border-radius: 24px;
    background: linear-gradient(90deg, var(--silver-dark) 0%, var(--silver-light) 18%, var(--white) 55%, #c9cbcf 100%);
    box-shadow: inset 0 -3px 0 rgba(0,0,0,.18);
    font-family: "Montserrat", sans-serif; font-weight: 500; font-size: 13px; color: var(--navy-mid);
    display: flex; align-items: center; justify-content: center; letter-spacing: .3px; text-decoration: none;
  }
</style>
</head>
<body>
  <div class="utility-bar">
    <a class="consult-link" href="#">Book a Sales Consultation ⟶</a>
    <span class="call-line">Call us now: <strong>555.014.2087</strong></span>
    <span class="bar-sep">|</span>
    <a class="map-link" href="#">Find us on the map ⟶</a>
    <a class="dashboard-link" href="#">My Korvane Dashboard</a>
    <span class="language">
      <svg width="15" height="10" viewBox="0 0 15 10" aria-hidden="true">
        <rect width="15" height="10" fill="#1f3a8a"/>
        <rect x="6" width="3" height="10" fill="#fff"/><rect y="3.5" width="15" height="3" fill="#fff"/>
        <rect x="6.8" width="1.4" height="10" fill="#c8102e"/><rect y="4.3" width="15" height="1.4" fill="#c8102e"/>
      </svg>
      English (English)
    </span>
  </div>

  <header class="site-header">
    <div class="brand"><span class="brand-dot"></span>Korvane</div>
    <nav class="main-nav">
      <a href="#" style="left:354px">Home</a>
      <a href="#" style="left:412px">Products</a>
      <a href="#" style="left:487px">Our Company</a>
      <a href="#" style="left:592px">Customer Resources</a>
      <a href="#" style="left:740px">Contact Us</a>
      <a href="#" style="left:829px">Online Ordering</a>
      <a href="#" style="left:945px">Hello, administrator</a>
    </nav>
    <svg class="cart" width="20" height="20" viewBox="0 0 20 20" aria-label="Cart">
      <path d="M2 7h16l-1.5 12h-13z" fill="none" stroke="#333" stroke-width="1.5" stroke-linejoin="round"/>
      <path d="M6.5 9V5a3.5 3.5 0 0 1 7 0v4" fill="none" stroke="#333" stroke-width="1.5"/>
    </svg>
    <span class="cart-badge">2</span>
  </header>

  <section class="hero">
    <div class="hero-dark"></div>
    <svg class="hero-bands" width="829" height="675" viewBox="0 0 829 675" aria-hidden="true">
      <polygon points="290,0 400,0 0,560 0,420" fill="rgba(255,255,255,0.035)"/>
      <polygon points="520,0 560,0 140,675 100,675" fill="rgba(255,255,255,0.025)"/>
      <polygon points="700,380 829,200 829,380 620,675 470,675" fill="rgba(255,255,255,0.02)"/>
    </svg>
    <div class="hero-light"></div>
    <div class="product-reflection" role="img" aria-label="Faint reflection of the alternator on a glossy floor"></div>
    <div class="product-photo" role="img" aria-label="Photo of a silver remanufactured alternator with pulley and copper windings"></div>

    <h1 class="hero-title">Korvane</h1>
    <p class="hero-copy">Lorem ipsum dolor sit amet, consectetur adipiscing elit, sed do eiusmod tempor incididunt ut labore et dolore magna aliqua. Quis ipsum suspendisse ultrices gravida</p>

    <div class="stats">
      <div class="stat"><span class="stat-value">25</span><span class="stat-label">FEATURE</span><span class="stat-note">Description</span></div>
      <div class="stat"><span class="stat-value">10</span><span class="stat-label">FEATURE</span><span class="stat-note">Description</span></div>
      <div class="stat"><span class="stat-value">02</span><span class="stat-label">FEATURE</span><span class="stat-note">Description</span></div>
    </div>

    <a class="cta" href="#">KNOW MORE</a>
  </section>
</body>
</html>
```